Wine Label Design for Ferrant Estate

I need a front and back label for a new wine I am making. I am looking for a classic, elegant and serious wine label. I would like the label to be white with blue and black writing. The blue will be the distinction in the label. The color of blue will be unique and catch the eye. The font of the writing will be unique and could also serve as the brand image for Ferrant Estate. The label can have a design but should be simple and distinct. I envision the paper quality of the label to textured, high quality and add to the overall image of the label.
The label will be timeless. The price of this wine will be $85.00 a bottle, and the label should match a higher priced wine. This wine is family owned and operated.
The writing on the front and back label will be:

FRONT Label-

Ferrant Estate

Howell Mountain

Napa Valley

2022 Cabernet Sauvignon

Back Label-

Cellared and Bottled by Ferrant Estate, Larkmoor, CA 94599

GOVERNMENT WARNING: (1) According to the Surgeon General, women should not drink alcoholic beverages during pregnancy because of the risk of birth defects. (2) Consumption of alcoholic beverages impairs your ability to drive a car or operate machinery, and may cause health problems.

Alc. 14.5% by Vol.

750 ml

Contains Sulfites

```html
<!DOCTYPE html>
<html lang="en">
<head>
<meta charset="utf-8">
<title>Ferrant Estate — Wine Labels</title>
<link href="https://fonts.googleapis.com/css2?family=Cinzel:wght@400;600&family=Marcellus&family=Cormorant+Garamond:wght@400;500&display=swap" rel="stylesheet">
<style>
  :root {
    --page: #ffffff;
    --paper: #fbfaf6;
    --paper-shade: #f1efe8;
    --ink: #161616;
    --accent: #1f4fa0;
    --ornament-a: #dfe5ee;
    --ornament-b: #c3cedd;
    --rule: #8fa6cc;
  }
  * { box-sizing: border-box; margin: 0; padding: 0; }
  html, body {
    width: 785px; height: 1200px; overflow: hidden;
    background: var(--page);
  }
  .canvas { position: relative; width: 785px; height: 1200px; }

  .label {
    position: absolute; top: 121px;
    width: 316px; height: 360px;
    background: radial-gradient(ellipse at 50% 40%, var(--paper) 55%, var(--paper-shade) 100%);
    color: var(--ink);
    border: 1px solid #e4e1d8;
    box-shadow: 0 14px 12px -8px rgba(0,0,0,0.25);
    font-family: "Marcellus", serif;
  }
  .label--front { left: 52px; }
  .label--back { left: 417px; }

  .ornament-frame {
    position: absolute; left: 29px; top: 12px; width: 258px; height: 335px;
    border: 22px solid transparent;
    border-image: linear-gradient(135deg, var(--ornament-b), var(--ornament-a) 50%, var(--ornament-b)) 1;
  }

  .line {
    position: absolute; left: 0; width: 100%;
    text-align: center; line-height: 1; white-space: nowrap;
    transform: translateY(-50%);
  }
  .accent { color: var(--accent); }
  .rule {
    position: absolute; left: 50%; height: 1px; transform: translateX(-50%);
    background: linear-gradient(90deg, transparent, var(--rule) 25%, var(--accent) 50%, var(--rule) 75%, transparent);
  }

  /* front */
  .brand-arc { position: absolute; left: 40px; top: 40px; width: 236px; height: 60px; }
  .brand-arc text { font-family: "Cinzel", serif; font-size: 34px; fill: var(--accent); letter-spacing: 3px; }
  .estate-word { top: 92px; font-family: "Cinzel", serif; font-weight: 600; font-size: 13px; letter-spacing: 2px; }
  .vintage-small { top: 109px; font-family: "Cormorant Garamond", serif; font-size: 14px; }
  .vineyard-scene {
    position: absolute; left: 73px; top: 119px; width: 165px; height: 102px;
    border-radius: 50%;
    background: radial-gradient(ellipse at 50% 55%, #e9edf3 0%, #c4cfde 60%, #f4f3ee 100%);
  }
  .region { top: 239px; font-family: "Cinzel", serif; font-size: 12.5px; letter-spacing: 1.6px; }
  .valley { top: 258px; font-size: 11px; letter-spacing: 2px; }
  .vintage { top: 280px; font-family: "Cinzel", serif; font-size: 13px; letter-spacing: 2px; }
  .varietal { top: 302px; font-size: 11.5px; letter-spacing: 1.8px; }

  /* back */
  .bottler-intro { top: 67px; font-size: 11px; letter-spacing: 1.8px; }
  .bottler-name { top: 97px; font-size: 16px; letter-spacing: 2.5px; }
  .bottler-address { top: 120px; font-family: "Cormorant Garamond", serif; font-size: 12.5px; }
  .warning {
    position: absolute; left: 67px; top: 155px; width: 182px;
    font-family: "Cormorant Garamond", serif; font-weight: 500; font-size: 6.4px; line-height: 9.6px;
    text-transform: uppercase; letter-spacing: -0.05px;
  }
  .warning-title { text-decoration: underline; }
  .sulfites { top: 257px; font-size: 10px; letter-spacing: 1.6px; }
  .alc { position: absolute; left: 72px; top: 277px; width: 62px; text-align: center; }
  .alc-word { display: block; font-size: 19px; letter-spacing: 1.5px; line-height: 1; }
  .alc-value { display: block; font-size: 7px; letter-spacing: 1px; margin-top: 3px; }
  .volume { position: absolute; left: 165px; top: 284px; font-size: 18px; letter-spacing: 2px; line-height: 1; }
</style>
</head>
<body>
<main class="canvas">

  <section class="label label--front" aria-label="Front label">
    <div class="ornament-frame" role="img" aria-label="Hand-drawn foliage border"></div>
    <svg class="brand-arc" viewBox="0 0 236 60" aria-label="Ferrant">
      <path id="brandCurve" d="M8 58 Q118 8 228 58" fill="none"/>
      <text text-anchor="middle"><textPath href="#brandCurve" startOffset="50%">FERRANT</textPath></text>
    </svg>
    <p class="line estate-word">-ESTATE-</p>
    <p class="line vintage-small">2022</p>
    <div class="vineyard-scene" role="img" aria-label="Engraved vineyard landscape with farmhouse, cypress trees and hills"></div>
    <div class="rule" style="top:227px;width:130px"></div>
    <p class="line region accent">-HOWELL MOUNTAIN-</p>
    <p class="line valley">NAPA VALLEY</p>
    <p class="line vintage">2022</p>
    <div class="rule" style="top:291px;width:90px"></div>
    <p class="line varietal accent">CABERNET SAUVIGNON</p>
  </section>

  <section class="label label--back" aria-label="Back label">
    <div class="ornament-frame" role="img" aria-label="Hand-drawn foliage border"></div>
    <p class="line bottler-intro">CELLARED AND BOTTLED BY</p>
    <p class="line bottler-name accent">FERRANT ESTATE</p>
    <p class="line bottler-address">LARKMOOR, CA 94599</p>
    <div class="rule" style="top:139px;width:130px"></div>
    <p class="warning">
      <span class="warning-title">Government Warning:</span><br>
      (1) According to the Surgeon General, women should not drink alcoholic beverages during pregnancy because of the risk of birth defects.<br>
      (2) Consumption of alcoholic beverages impairs your ability to drive a car or operate machinery, and may cause health problems.
    </p>
    <div class="rule" style="top:245px;width:130px"></div>
    <p class="line sulfites accent">-CONTAINS SULFITES-</p>
    <p class="alc"><span class="alc-word">ALC</span><span class="alc-value">14.5% BY VOL</span></p>
    <p class="volume">750 ML</p>
  </section>

</main>
</body>
</html>
```